A UK based Lettings and Property Management Company - Brindle Oak Property

Brindle Oak Property rents and manages properties on behalf of owners in Liverpool, UK. We are looking for a clean, fresh modern design which incororates our logo.

In terms of pages we initially require:

Home
Lettings
Property Management
Landlords
Tenants
About
Contact

In would like to use colours compatible with the logo

Target Market(s)

People looking to rent property
Owners looking to use our services to let their property

Industry/Entity Type

Property

Contact Information for Business Card

Logo prominent on one side
Address to be edited by us as we are moving premises in October
Name Gareth Whitlow
Tel number 0151 486 2037
e-mail gareth@brindleoakhomes.co.uk

Font styles to use
Sans Serif

Colors

Designer to choose colors to be used in the design.

Requirements
Must have
• Clean lines
• Fresh
• Easy navigation
• Easy editing
• Data capture

```html
<!DOCTYPE html>
<html lang="en">
<head>
<meta charset="utf-8">
<title>Brindle Oak Property – Properties for Rent</title>
<link href="https://fonts.googleapis.com/css2?family=Open+Sans:wght@400;600;700&display=swap" rel="stylesheet">
<style>
:root{
  --teal:#2a6a73;
  --teal-dark:#1f5860;
  --navy:#14144f;
  --navy-deep:#0f1046;
  --red:#ee1f45;
  --grey:#f1f1f1;
  --card-grey:#ececec;
  --text:#222;
  --white:#fff;
}
*{box-sizing:border-box;margin:0;padding:0}
html,body{width:1200px;height:3352px;overflow:hidden}
body{font-family:"Open Sans",Arial,sans-serif;color:var(--text);background:var(--white);position:relative}
.site-header{height:127px;display:flex;align-items:center;justify-content:space-between;padding:0 85px}
.brand{display:flex;align-items:center;gap:14px}
.brand-square{width:54px;height:54px;background:var(--navy)}
.brand-name{font-weight:700;font-size:26px;line-height:1.05;color:var(--navy);letter-spacing:1px;text-transform:uppercase}
.header-contacts{display:flex;gap:34px;align-items:center}
.header-item{display:flex;align-items:center;gap:14px;color:var(--teal)}
.header-item strong{display:block;font-weight:600;font-size:26px;line-height:1}
.header-item span{display:block;font-size:21px;color:var(--navy);line-height:1.2}
.main-nav{height:54px;background:var(--teal);display:flex;align-items:center;gap:38px;padding-left:85px}
.main-nav a{color:var(--white);text-decoration:none;font-size:16px;font-weight:600;text-transform:uppercase;display:flex;align-items:center;gap:7px}
.main-nav a i{display:inline-block;width:12px;height:12px;background:var(--white);border-radius:2px}
.hero{position:relative;height:478px;background:linear-gradient(100deg,#4a3a2c 0%,#7a5a3a 40%,#b08a5a 70%,#d8c2a0 100%);text-align:center;color:var(--white)}
.hero::after{content:"";position:absolute;inset:0;background:rgba(0,0,0,.35)}
.hero > *{position:relative;z-index:1}
.hero h1{padding-top:85px;font-size:42px;font-weight:700;letter-spacing:.5px}
.hero p{font-size:21px;font-weight:600;margin-top:2px;text-transform:uppercase}
.search-panel{position:absolute;left:123px;top:188px;width:945px;height:208px;background:rgba(42,106,115,.75);padding:36px 33px 0}
.search-row{display:flex;height:51px}
.search-input{flex:0 0 655px;background:var(--white);color:#555;text-align:left;padding-left:22px;font-size:16px;display:flex;align-items:center}
.search-btn{flex:1;background:var(--red);display:flex;align-items:center;justify-content:center;gap:12px;font-size:25px;font-weight:600}
.filter-row{display:flex;margin-top:20px;border:1px solid var(--white);height:80px}
.filter{flex:1;text-align:left;padding:14px 0 0 38px;font-size:16px;border-right:1px solid var(--white);position:relative}
.filter:last-child{border-right:none}
.filter b{display:block;font-weight:600}
.filter::after{content:"";position:absolute;right:20px;top:36px;width:7px;height:7px;border-right:2px solid #fff;border-bottom:2px solid #fff;transform:rotate(45deg)}
.section-title{text-align:center;position:relative}
.section-rule{display:block;width:360px;height:2px;margin:16px auto 0;background:var(--teal)}
.section-title h2{font-weight:400;font-size:30px;color:var(--navy);text-transform:uppercase;margin-top:4px}
.listings{padding-top:56px;height:1006px}
.card-grid{display:grid;grid-template-columns:repeat(3,322px);column-gap:31px;row-gap:38px;padding-left:85px;margin-top:45px}
.card{background:var(--card-grey);height:357px}
.card-photo{height:190px;background:linear-gradient(180deg,#8aa884 0%,#c9c7bd 45%,#77736a 100%);position:relative}
.card-type{position:absolute;left:6px;bottom:30px;background:var(--white);font-size:12px;padding:2px 8px}
.card-price{position:absolute;left:0;bottom:0;background:var(--teal);color:#fff;font-size:13px;padding:4px 8px}
.card-title{height:51px;display:flex;align-items:center;justify-content:center;font-size:17px;text-transform:uppercase}
.card-address{height:56px;background:var(--navy);color:#fff;text-align:center;font-size:13px;padding-top:9px;line-height:1.5}
.card-stats{display:flex;height:60px;align-items:center;font-size:12px;text-align:center}
.card-stats div{flex:1;border-right:1px solid #bbb;line-height:1.5}
.card-stats div:last-child{flex:1.6;border:none}
.newsletter{position:absolute;top:1665px;left:0;width:1200px;height:279px;background:linear-gradient(180deg,#3e7d86,#2d6a73);color:#fff;text-align:center}
.newsletter h2{font-weight:400;font-size:28px;padding-top:54px;text-transform:uppercase}
.newsletter p{font-size:17px;margin-top:10px}
.btn-outline{display:inline-block;margin-top:22px;width:334px;height:61px;line-height:57px;border:2px solid #fff;background:var(--navy);font-size:24px;text-transform:uppercase}
.areas{position:absolute;top:1944px;left:0;width:1200px;height:447px;background:var(--grey);padding-top:70px}
.area-grid{display:flex;gap:29px;padding-left:89px;margin-top:26px}
.area{width:322px;height:186px;background:linear-gradient(180deg,#3a3f6e,#2b2d5a);color:#fff;display:flex;align-items:center;justify-content:center;font-size:26px;text-transform:uppercase}
.testimonials{position:absolute;top:2391px;left:0;width:1200px;height:497px;padding-top:67px;text-align:center}
.avatar{width:108px;height:108px;border-radius:50%;border:3px solid #ddd;background:linear-gradient(160deg,#c9a58a,#6b4f3e);margin:43px auto 0}
.quote{position:relative;width:870px;margin:24px auto 0;font-size:18px;line-height:1.6;color:#333}
.quote-mark{position:absolute;left:-46px;top:-6px}
.cite{margin-top:28px;font-weight:700;font-size:18px;color:#222;line-height:1.25}
.arrow{position:absolute;top:292px;width:32px;height:32px;border-radius:50%;background:var(--navy-deep)}
.arrow.prev{left:38px}.arrow.next{right:38px}
.site-footer{position:absolute;top:2888px;left:0;width:1200px;height:420px;background:linear-gradient(180deg,#1a1b6e,#14155a);color:#fff}
.footer-brand{display:flex;align-items:center;justify-content:center;gap:16px;padding-top:62px}
.footer-brand .brand-square{background:#fff;width:64px;height:64px}
.footer-brand .brand-name{color:#fff;font-size:34px}
.social{display:flex;justify-content:center;gap:16px;margin-top:48px}
.social span{width:44px;height:44px;border-radius:50%;background:var(--teal)}
.footer-contacts{display:flex;justify-content:space-between;padding:0 80px 0 116px;margin-top:52px;font-size:22px;line-height:1.45}
.footer-contacts div{display:flex;gap:22px;align-items:center}
.copyright{position:absolute;top:3308px;left:0;width:1200px;height:44px;background:var(--teal);color:#fff;font-size:17px;text-align:center;line-height:44px}
</style>
</head>
<body>
<header class="site-header">
  <div class="brand"><span class="brand-square"></span><span class="brand-name">Brindle Oak<br>Property</span></div>
  <div class="header-contacts">
    <div class="header-item">
      <svg width="46" height="46" viewBox="0 0 24 24" fill="none" stroke="currentColor" stroke-width="1.6"><path d="M5 3h4l2 5-3 2a12 12 0 0 0 6 6l2-3 5 2v4a2 2 0 0 1-2 2A17 17 0 0 1 3 5a2 2 0 0 1 2-2z"/></svg>
      <div><strong>Phone Number</strong><span>+ 0151 486 2037</span></div>
    </div>
    <div class="header-item">
      <svg width="62" height="46" viewBox="0 0 32 24" fill="none" stroke="currentColor" stroke-width="1.6"><rect x="1" y="1" width="30" height="22" rx="2"/><path d="M1 2l15 12L31 2"/></svg>
      <div><strong>Schedule An</strong><span>Appointment</span></div>
    </div>
  </div>
</header>
<nav class="main-nav">
  <a href="#"><i></i>Home</a><a href="#"><i></i>Lettings</a><a href="#"><i></i>Property Management</a><a href="#"><i></i>Landlords</a><a href="#"><i></i>Tenants</a><a href="#"><i></i>About</a><a href="#"><i></i>Contact</a>
</nav>
<section class="hero" role="img" aria-label="Photo of a furnished living room interior">
  <h1>DISCOVER PROPERTIES FOR RENT</h1>
  <p>The simple way to search for property to rent in the UK</p>
  <form class="search-panel">
    <div class="search-row">
      <div class="search-input">E.G.BRISTOL,SW6, G61 2DW, VICTORIA STATION</div>
      <div class="search-btn"><svg width="22" height="22" viewBox="0 0 24 24" fill="none" stroke="#fff" stroke-width="3"><circle cx="10" cy="10" r="7"/><path d="M15 15l7 7"/></svg>SEARCH</div>
    </div>
    <div class="filter-row">
      <div class="filter"><b>MIN PRICE (£)</b>Any</div>
      <div class="filter"><b>MAX PRICE (£)</b>Any</div>
      <div class="filter"><b>MIN PRICE (£)</b>Any</div>
      <div class="filter"><b>MAX PRICE (£)</b>Any</div>
    </div>
  </form>
</section>

<section class="listings">
  <div class="section-title">
    <span class="section-rule"></span>
    <h2>New Rental Properties</h2>
  </div>
  <div class="card-grid">
    <article class="card"><div class="card-photo" role="img" aria-label="Photo of a terraced house with balconies"><span class="card-type">Residential</span><span class="card-price">£285,000</span></div><div class="card-title">27 Elm Grove</div><div class="card-address">ELM GROVE 27<br>Liverpool, Merseyside L15 4JT</div><div class="card-stats"><div>3<br>Beds</div><div>2<br>Baths</div><div>1,383<br>Square Feet</div></div></article>
    <article class="card"><div class="card-photo" role="img" aria-label="Photo of a terraced house with balconies"><span class="card-type">Residential</span><span class="card-price">£285,000</span></div><div class="card-title">27 Elm Grove</div><div class="card-address">ELM GROVE 27<br>Liverpool, Merseyside L15 4JT</div><div class="card-stats"><div>3<br>Beds</div><div>2<br>Baths</div><div>1,383<br>Square Feet</div></div></article>
    <article class="card"><div class="card-photo" role="img" aria-label="Photo of a terraced house with balconies"><span class="card-type">Residential</span><span class="card-price">£285,000</span></div><div class="card-title">27 Elm Grove</div><div class="card-address">ELM GROVE 27<br>Liverpool, Merseyside L15 4JT</div><div class="card-stats"><div>3<br>Beds</div><div>2<br>Baths</div><div>1,383<br>Square Feet</div></div></article>
    <article class="card"><div class="card-photo" role="img" aria-label="Photo of a terraced house with balconies"><span class="card-type">Residential</span><span class="card-price">£285,000</span></div><div class="card-title">27 Elm Grove</div><div class="card-address">ELM GROVE 27<br>Liverpool, Merseyside L15 4JT</div><div class="card-stats"><div>3<br>Beds</div><div>2<br>Baths</div><div>1,383<br>Square Feet</div></div></article>
    <article class="card"><div class="card-photo" role="img" aria-label="Photo of a terraced house with balconies"><span class="card-type">Residential</span><span class="card-price">£285,000</span></div><div class="card-title">27 Elm Grove</div><div class="card-address">ELM GROVE 27<br>Liverpool, Merseyside L15 4JT</div><div class="card-stats"><div>3<br>Beds</div><div>2<br>Baths</div><div>1,383<br>Square Feet</div></div></article>
    <article class="card"><div class="card-photo" role="img" aria-label="Photo of a terraced house with balconies"><span class="card-type">Residential</span><span class="card-price">£285,000</span></div><div class="card-title">27 Elm Grove</div><div class="card-address">ELM GROVE 27<br>Liverpool, Merseyside L15 4JT</div><div class="card-stats"><div>3<br>Beds</div><div>2<br>Baths</div><div>1,383<br>Square Feet</div></div></article>
  </div>
</section>

<section class="newsletter" role="img" aria-label="Faded photo of a grand country house behind a teal overlay">
  <h2>Stay Up-To-Date With Our Latest Listings</h2>
  <p>Be The First To Know When New Properties Hit The Market</p>
  <span class="btn-outline">Get Started</span>
</section>

<section class="areas">
  <div class="section-title">
    <span class="section-rule"></span>
    <h2>Featured Areas</h2>
  </div>
  <div class="area-grid">
    <div class="area" role="img" aria-label="Photo of Virginia Water houses">Virginia Water</div>
    <div class="area" role="img" aria-label="Photo of a Beaconsfield house">Beaconsfield</div>
    <div class="area" role="img" aria-label="Photo of Keston street">Keston</div>
  </div>
</section>

<section class="testimonials">
  <div class="section-title">
    <span class="section-rule"></span>
    <h2>What Customers Say About Us</h2>
  </div>
  <div class="avatar" role="img" aria-label="Customer portrait photo"></div>
  <blockquote class="quote">
    <svg class="quote-mark" width="28" height="22" viewBox="0 0 28 22" fill="#2a6a73"><rect x="0" y="6" width="11" height="11" rx="2"/><rect x="15" y="6" width="11" height="11" rx="2"/><path d="M2 8Q3 1 11 0v3Q6 4 5 8zM17 8Q18 1 26 0v3Q21 4 20 8z"/></svg>
    Thanks for being so pro-active to help us buy our dream home. There were many other buyers<br>interested but you helped guide us through the bidding process and worked your magic!
  </blockquote>
  <p class="cite">Hannah Pryce<br>Buyer</p>
  <span class="arrow prev"><svg width="32" height="32" viewBox="0 0 32 32"><path d="M19 9l-7 7 7 7" stroke="#fff" stroke-width="3" fill="none"/></svg></span>
  <span class="arrow next"><svg width="32" height="32" viewBox="0 0 32 32"><path d="M13 9l7 7-7 7" stroke="#fff" stroke-width="3" fill="none"/></svg></span>
</section>

<footer class="site-footer">
  <div class="footer-brand"><span class="brand-square"></span><span class="brand-name">Brindle Oak<br>Property</span></div>
  <div class="social"><span></span><span></span><span></span><span></span><span></span><span></span></div>
  <div class="footer-contacts">
    <div><svg width="34" height="50" viewBox="0 0 24 34" fill="none" stroke="#3fa3a8" stroke-width="2"><path d="M12 33S2 20 2 12a10 10 0 0 1 20 0c0 8-10 21-10 21z"/><circle cx="12" cy="12" r="4"/></svg><span>48 Harbour Row,<br>Suite 12</span></div>
    <div><svg width="44" height="44" viewBox="0 0 24 24" fill="none" stroke="#3fa3a8" stroke-width="1.6"><path d="M5 3h4l2 5-3 2a12 12 0 0 0 6 6l2-3 5 2v4a2 2 0 0 1-2 2A17 17 0 0 1 3 5a2 2 0 0 1 2-2z"/></svg><span>0151 486 2037<br>0151 486 2037</span></div>
    <div><svg width="56" height="42" viewBox="0 0 32 24" fill="none" stroke="#3fa3a8" stroke-width="1.6"><rect x="1" y="1" width="30" height="22" rx="2"/><path d="M1 2l15 12L31 2"/></svg><span>info@brindleoakhomes.co.uk<br>info@brindleoakhomes.co.uk</span></div>
  </div>
</footer>
<div class="copyright">© 2016 BrindleOakHomes.co.uk</div>
</body>
</html>
```